Website for Boutique Property Consultancy in UK

We are looking to designing a website for our Property Consultancy Services that follows a minimalistic clean style that is also bold and intriguing.
The website will be based on one landing page and a link to Connect Page and email link.

Dominant features will be the company logo or icon and colours.

Brand colours provided for guidance.

Looking to achieve a minimalistic clean style that is also bold and intriguing.

"Updated"
Page 1 - Landing Page with the Hyperlinks to Pick a Service, Training Portal and Maple Nine Portal. example landing page https://tilbrook-studio.co.uk/

Page 2 - Shows all the Services and Sectors

Target Market(s)

Occupier Clients, Tech Companies, Property Developers, Infrastructure Clients and Major Consultants

Industry/Entity Type

Construction

Coding

Coded - Design and coding required

Number of Pages Required

2 page

Font styles to use
Other font styles liked:
• Century Gothic or Futuris (Headings)

Colors
0054AA
0677BA
7BADD7
CADEEF
E8F1F8
00AB8E
00BBA5
67D7C9
C6EFE9
E9F9F6

Requirements
Must have
• Company Logo, link to enquiry and Connect

```html
<!DOCTYPE html>
<html lang="en">
<head>
<meta charset="utf-8">
<title>Halden Reeve – Brand Board</title>
<link rel="stylesheet" href="https://fonts.googleapis.com/css2?family=Urbanist:wght@300;400;700&display=swap">
<style>
  :root {
    --green: #1ec075;
    --navy: #131338;
    --mist: #e9e9eb;
    --ink-soft: #3a3a55;
    --white: #ffffff;
    --rule: #c9c9cf;
  }
  * { margin: 0; padding: 0; box-sizing: border-box; }
  html, body { width: 888px; height: 1200px; overflow: hidden; }
  body {
    position: relative;
    background: var(--mist);
    font-family: "Urbanist", "Century Gothic", sans-serif;
    color: var(--navy);
  }

  /* Brand guide header */
  .guide-logo {
    position: absolute; left: 173px; top: 100px;
    font-size: 18px; font-weight: 400; letter-spacing: 0.3px;
    color: var(--navy);
  }
  .guide-rule { position: absolute; top: 80px; width: 1px; height: 68px; background: var(--rule); }
  .guide-rule--one { left: 360px; }
  .guide-rule--two { left: 583px; }
  .guide-fonts { position: absolute; left: 431px; top: 76px; }
  .guide-title { font-size: 20px; font-weight: 400; color: var(--navy); line-height: 1; }
  .guide-fontname { margin-top: 18px; font-size: 12.5px; font-weight: 400; color: var(--ink-soft); }
  .guide-colors { position: absolute; left: 655px; top: 75px; }
  .swatches { position: absolute; left: 0; top: 27px; display: flex; gap: 8px; }
  .swatch { width: 31px; text-align: center; }
  .swatch-dot { width: 31px; height: 31px; border-radius: 50%; box-shadow: 0 1px 3px rgba(0,0,0,.12); }
  .swatch-dot--green { background: var(--green); }
  .swatch-dot--navy { background: var(--navy); }
  .swatch-dot--mist { background: #f1f1f3; }
  .swatch-code { display: block; margin-top: 4px; margin-left: -4px; width: 39px; font-size: 7px; color: var(--ink-soft); letter-spacing: 0.2px; }

  /* Landing page */
  .site {
    position: absolute; width: 703px; height: 440px; overflow: hidden;
    color: var(--white);
  }
  .site--preview { left: 165px; top: 216px; transform: scale(0.832); transform-origin: top left; }
  .site--full { left: 103px; top: 684px; }
  .site-photo {
    position: absolute; inset: 0;
    background:
      radial-gradient(ellipse 90px 40px at 505px 70px, rgba(20,20,22,.55), rgba(20,20,22,0)),
      radial-gradient(ellipse 160px 120px at 480px 130px, rgba(160,160,163,.35), rgba(160,160,163,0)),
      linear-gradient(172deg, rgba(18,18,20,.55) 0%, rgba(18,18,20,.15) 30%, rgba(18,18,20,0) 45%),
      linear-gradient(90deg, #1e1e20 0%, #2e2e31 18%, #3b3b3e 38%, #5f5f62 48%, #7a7a7d 53%, #6d6d70 58%, #39393c 66%, #2a2a2d 82%, #1b1b1d 100%);
  }
  .site-shade {
    position: absolute; inset: 0;
    background: linear-gradient(180deg, rgba(0,0,0,.25) 0%, rgba(0,0,0,0) 18%, rgba(0,0,0,0) 70%, rgba(0,0,0,.3) 100%);
  }
  .site-header { position: absolute; left: 0; right: 0; top: 0; height: 38px; border-bottom: 1px solid rgba(255,255,255,.08); }
  .site-logo { position: absolute; left: 65px; top: 11px; font-size: 12px; font-weight: 400; color: var(--white); letter-spacing: 0.3px; }
  .site-nav { position: absolute; left: 286px; top: 13px; display: flex; gap: 18px; font-size: 7px; }
  .site-nav a { color: var(--white); text-decoration: none; }
  .site-follow { position: absolute; left: 578px; top: 14px; font-size: 6.5px; color: rgba(255,255,255,.7); }
  .site-social {
    position: absolute; left: 618px; top: 8px; width: 20px; height: 20px; border-radius: 50%;
    background: var(--green); display: flex; align-items: center; justify-content: center;
  }
  .site-social svg { width: 9px; height: 9px; }
  .hero { position: absolute; left: 65px; top: 244px; }
  .hero-kicker { font-size: 6px; letter-spacing: 3.2px; text-transform: uppercase; color: var(--green); }
  .hero-title { margin-top: 6px; font-size: 23px; font-weight: 300; line-height: 27px; letter-spacing: 0.2px; }
  .hero-title strong { font-weight: 700; }
  .hero-contact { margin-top: 13px; font-size: 7.5px; }
  .hero-badge {
    margin-top: 17px; width: 16px; height: 16px; border-radius: 50%;
    border: 1.5px solid rgba(255,255,255,.9);
  }
</style>
</head>
<body>
  <header class="guide">
    <div class="guide-logo">halden reeve</div>
    <span class="guide-rule guide-rule--one"></span>
    <div class="guide-fonts">
      <h2 class="guide-title">Fonts</h2>
      <p class="guide-fontname">Century Gothic</p>
    </div>
    <span class="guide-rule guide-rule--two"></span>
    <div class="guide-colors">
      <h2 class="guide-title">Colors:</h2>
      <div class="swatches">
        <div class="swatch"><div class="swatch-dot swatch-dot--green"></div><span class="swatch-code">#1ec075</span></div>
        <div class="swatch"><div class="swatch-dot swatch-dot--navy"></div><span class="swatch-code">#131338</span></div>
        <div class="swatch"><div class="swatch-dot swatch-dot--mist"></div><span class="swatch-code">#e9e9eb</span></div>
      </div>
    </div>
  </header>

  <section class="site site--preview">
    <div class="site-photo" role="img" aria-label="Black and white upward view of glass office towers against a cloudy sky"></div>
    <div class="site-shade"></div>
    <div class="site-header">
      <div class="site-logo">halden reeve</div>
      <nav class="site-nav"><a href="#">Pick a Service</a><a href="#">Training Portal</a><a href="#">Maple Nine</a></nav>
      <span class="site-follow">Follow Us:</span>
      <a class="site-social" href="#" aria-label="Follow us">
        <svg viewBox="0 0 10 10"><path d="M2 8 L8 2 M3.5 2 H8 V6.5" fill="none" stroke="#131338" stroke-width="1.6" stroke-linecap="round" stroke-linejoin="round"/></svg>
      </a>
    </div>
    <div class="hero">
      <p class="hero-kicker">Welcome to halden reeve</p>
      <h1 class="hero-title">Delivering <strong>Value</strong> and<br>Redefining <strong>Boundaries</strong></h1>
      <p class="hero-contact">By Referral Only &nbsp;|&nbsp; Email/Connect</p>
      <div class="hero-badge"></div>
    </div>
  </section>

  <section class="site site--full">
    <div class="site-photo" role="img" aria-label="Black and white upward view of glass office towers against a cloudy sky"></div>
    <div class="site-shade"></div>
    <div class="site-header">
      <div class="site-logo">halden reeve</div>
      <nav class="site-nav"><a href="#">Pick a Service</a><a href="#">Training Portal</a><a href="#">Maple Nine</a></nav>
      <span class="site-follow">Follow Us:</span>
      <a class="site-social" href="#" aria-label="Follow us">
        <svg viewBox="0 0 10 10"><path d="M2 8 L8 2 M3.5 2 H8 V6.5" fill="none" stroke="#131338" stroke-width="1.6" stroke-linecap="round" stroke-linejoin="round"/></svg>
      </a>
    </div>
    <div class="hero">
      <p class="hero-kicker">Welcome to halden reeve</p>
      <h1 class="hero-title">Delivering <strong>Value</strong> and<br>Redefining <strong>Boundaries</strong></h1>
      <p class="hero-contact">By Referral Only &nbsp;|&nbsp; Email/Connect</p>
      <div class="hero-badge"></div>
    </div>
  </section>
</body>
</html>
```